Trade Show Booth Design for Saas company

Brightpost Suite is a startup company that will be launching its software as a service product at a trade show in the near future. We are looking for something that really pops and is appealing to the eye. Attached is the branding guidelines along with the color palette. The pink should be predominant. We’re not so concerned with the copy of your design for the contest, but rather the design itself. We can work on the copy later. You can utilize any copy or graphics from our website at www.brightpostsuite.example. You can also learn more about us at the website. One element from the website that is worth mentioning, and optional, is the hub and spoke graphic in the “Connect All Your SMTP Email Service Providers” section. (It is attached.) We will provide high resolution versions of anything you need. The display will be a flat 10 foot wide by 8 foot tall, one piece of fabric. We will also need the graphics for the 39in x 19in x 12in Counter Graphic Print, but probably just the logo on it. We are open to design elements that include the use of a person or not. We basically want something modern and very eye-catching.
Potential headline and text:
One place to manage it all
Guided by expert mailers, Brightpost Suite combines every aspect of email marketing into a powerful package.

```html
<!DOCTYPE html>
<html lang="en">
<head>
<meta charset="utf-8">
<title>Brightpost Suite – Trade Show Graphics</title>
<link href="https://fonts.googleapis.com/css2?family=Montserrat:wght@500;600;700;800&display=swap" rel="stylesheet">
<style>
  :root{
    --navy:#161a45;
    --pink:#ff3d8b;
    --pink-soft:#fde6ef;
    --lavender:#eef0fb;
    --white:#ffffff;
    --stage:#d4d4d6;
    --label:#1a1a1a;
  }
  *{box-sizing:border-box;margin:0;padding:0}
  html,body{width:1200px;height:2198px;overflow:hidden}
  body{background:var(--stage);font-family:"Montserrat",sans-serif;position:relative}

  .backdrop{position:absolute;left:100px;top:200px;width:1000px;height:1000px;overflow:hidden;
    background:linear-gradient(120deg,var(--lavender) 0%,#f6ecf6 50%,var(--pink-soft) 100%);
    box-shadow:0 6px 18px rgba(0,0,0,.18)}
  .backdrop__band{position:absolute;left:0;top:618px;width:100%;height:382px;background:var(--navy)}
  .backdrop__band-texture{position:absolute;left:0;top:700px;width:100%;height:300px;
    background:radial-gradient(ellipse at 40% 60%,rgba(60,70,130,.35),rgba(22,26,69,0) 70%)}
  .corner{position:absolute;width:114px;height:114px}
  .corner--top-right{right:0;top:0;border-top:34px solid var(--navy);border-right:34px solid var(--navy)}
  .corner--bottom-left{left:0;bottom:0;border-bottom:34px solid var(--white);border-left:34px solid var(--white)}

  .brand{position:absolute;left:0;width:100%;display:flex;justify-content:center;align-items:center;gap:14px;
    font-weight:700;color:var(--navy)}
  .brand__square{background:var(--pink)}
  .backdrop .brand{top:70px;font-size:44px}
  .backdrop .brand__square{width:40px;height:40px}

  .headline{position:absolute;left:0;width:100%;text-align:center;font-weight:800;letter-spacing:3px;line-height:1}
  .headline--top{top:238px;font-size:80px;color:var(--navy)}
  .headline--bottom{top:312px;font-size:86px;color:var(--pink)}
  .intro{position:absolute;left:0;top:412px;width:100%;text-align:center;font-weight:600;font-size:25px;
    letter-spacing:1px;line-height:1.3;color:var(--navy)}

  .features{position:absolute;left:34px;top:535px;width:933px;display:grid;
    grid-template-columns:repeat(3,299px);grid-template-rows:81px 82px;column-gap:18px;row-gap:2px}
  .feature{display:flex;align-items:center;gap:18px;padding-left:16px;font-weight:700;font-size:22px;
    letter-spacing:.8px;line-height:1.15}
  .feature--pink{background:var(--pink);color:var(--white)}
  .feature--navy{background:var(--navy);color:var(--white)}
  .feature--light{background:var(--white);color:var(--navy)}
  .feature__icon{width:50px;height:50px;flex:none;display:flex;align-items:center;justify-content:center}
  .feature--pink .feature__icon,.feature--navy .feature__icon{background:var(--white)}
  .feature--light .feature__icon{background:var(--navy)}
  .feature__icon svg{width:30px;height:30px}

  .contacts{position:absolute;left:34px;top:756px;width:932px;display:flex;align-items:center;
    justify-content:space-between;color:var(--white)}
  .contact{display:flex;align-items:center;gap:10px}
  .contact__icon{width:34px;height:34px;flex:none;background:var(--pink);display:flex;align-items:center;justify-content:center}
  .contact__icon svg{width:22px;height:22px}
  .contact__label{font-size:13px;font-weight:700;letter-spacing:1px}
  .contact__value{font-size:15px;font-weight:500;letter-spacing:.5px;white-space:nowrap}
  .contact__value strong{font-weight:700}
  .contacts__divider{width:2px;height:36px;flex:none;background:rgba(255,255,255,.7)}

  .size-label{position:absolute;left:0;width:100%;text-align:center;font-weight:500;font-size:50px;color:var(--label);letter-spacing:1px}
  .size-label--wall{top:1238px}
  .size-label--counter{top:1860px}

  .counter{position:absolute;left:108px;top:1390px;width:984px;height:366px;overflow:hidden;
    background:linear-gradient(100deg,#b6ece6 0%,#e5e6f4 30%,#f1dcef 60%,#fbd2e2 100%);
    box-shadow:0 6px 18px rgba(0,0,0,.18)}
  .counter__texture{position:absolute;inset:0;
    background:radial-gradient(ellipse at 35% 40%,rgba(255,255,255,.45),rgba(255,255,255,0) 60%)}
  .counter .brand{top:150px;font-size:48px}
  .counter .brand__square{width:44px;height:44px}
</style>
</head>
<body>

<section class="backdrop" aria-label="10 by 10 foot booth backdrop">
  <div class="backdrop__band"></div>
  <div class="backdrop__band-texture" role="img" aria-label="Faint dotted world map texture"></div>
  <div class="corner corner--top-right"></div>
  <div class="corner corner--bottom-left"></div>

  <div class="brand"><span class="brand__square"></span><span>Brightpost Suite</span></div>

  <h1 class="headline headline--top">ONE PLACE</h1>
  <h2 class="headline headline--bottom">TO MANAGE IT ALL</h2>
  <p class="intro">Guided by expert mailers, Brightpost Suite combines every<br>aspect of email marketing into a powerful package.</p>

  <div class="features">
    <div class="feature feature--pink">
      <span class="feature__icon"><svg viewBox="0 0 30 30" fill="none" stroke="#ff3d8b" stroke-width="1.6"><path d="M8 3h10l5 5v19H8z"/><path d="M13 15l-2 2 2 2M17 15l2 2-2 2"/></svg></span>
      <span>Multiple SMTP<br>Connections</span>
    </div>
    <div class="feature feature--navy">
      <span class="feature__icon"><svg viewBox="0 0 30 30" fill="none" stroke="#161a45" stroke-width="1.6"><circle cx="15" cy="15" r="4"/><circle cx="15" cy="5" r="2"/><circle cx="15" cy="25" r="2"/><circle cx="5" cy="15" r="2"/><circle cx="25" cy="15" r="2"/><path d="M15 7v4M15 19v4M7 15h4M19 15h4"/></svg></span>
      <span>Email<br>Automation</span>
    </div>
    <div class="feature feature--navy">
      <span class="feature__icon"><svg viewBox="0 0 30 30" fill="none" stroke="#161a45" stroke-width="1.6"><rect x="4" y="5" width="18" height="18"/><path d="M8 18l4-5 3 3 4-5"/><rect x="15" y="17" width="11" height="8"/><path d="M15 17l5.5 4 5.5-4"/></svg></span>
      <span>Email<br>Validation</span>
    </div>
    <div class="feature feature--light">
      <span class="feature__icon"><svg viewBox="0 0 30 30" fill="none" stroke="#ffffff" stroke-width="1.8"><circle cx="12" cy="12" r="7"/><path d="M17 17l9 9"/></svg></span>
      <span>API<br>Connections</span>
    </div>
    <div class="feature feature--light">
      <span class="feature__icon"><svg viewBox="0 0 30 30" fill="none" stroke="#ffffff" stroke-width="1.6"><path d="M25 5c-7 0-12 5-14 11l3 3c6-2 11-7 11-14z"/><circle cx="19" cy="11" r="2"/><path d="M11 16l-5 1 3-5M14 19l-1 5 5-3M5 25l5-5"/></svg></span>
      <span>In-house<br>SMTP</span>
    </div>
    <div class="feature feature--light">
      <span class="feature__icon"><svg viewBox="0 0 30 30" fill="none" stroke="#ffffff" stroke-width="1.6"><rect x="4" y="4" width="22" height="15"/><path d="M9 15v-4M13 15V8M17 15v-5M21 15v-2M15 19v3M10 27l5-5 5 5"/></svg></span>
      <span>Reporting and<br>Analytics</span>
    </div>
  </div>

  <div class="contacts">
    <div class="contact">
      <span class="contact__icon"><svg viewBox="0 0 22 22" fill="none" stroke="#fff" stroke-width="1.5"><path d="M5 3l3 0 1.5 4-2 1.5a10 10 0 0 0 6 6l1.5-2 4 1.5v3c0 1-1 2-2 2A16 16 0 0 1 3 5c0-1 1-2 2-2z"/></svg></span>
      <div><div class="contact__label">PHONE</div><div class="contact__value"><strong>+1 (555) 014-2290</strong></div></div>
    </div>
    <span class="contacts__divider"></span>
    <div class="contact">
      <span class="contact__icon"><svg viewBox="0 0 22 22" fill="none" stroke="#fff" stroke-width="1.4"><circle cx="11" cy="11" r="8"/><ellipse cx="11" cy="11" rx="3.5" ry="8"/><path d="M3 11h16"/></svg></span>
      <div><div class="contact__label">WEBSITE</div><div class="contact__value">WWW.<strong>BRIGHTPOSTSUITE</strong>.EXAMPLE</div></div>
    </div>
    <span class="contacts__divider"></span>
    <div class="contact">
      <span class="contact__icon"><svg viewBox="0 0 22 22" fill="none" stroke="#fff" stroke-width="1.4"><rect x="3" y="5" width="16" height="12"/><path d="M3 5l8 6 8-6"/></svg></span>
      <div><div class="contact__label">EMAIL</div><div class="contact__value">INFO@<strong>BRIGHTPOSTSUITE</strong>.EXAMPLE</div></div>
    </div>
  </div>
</section>

<p class="size-label size-label--wall">10 Foot &nbsp;x&nbsp; 10 Foot</p>

<section class="counter" aria-label="Counter graphic print">
  <div class="counter__texture" role="img" aria-label="Faint dotted world map over a soft mint-to-pink gradient"></div>
  <div class="brand"><span class="brand__square"></span><span>Brightpost Suite</span></div>
</section>

<p class="size-label size-label--counter">39in &nbsp;x&nbsp; 19in &nbsp;x&nbsp; 12in</p>

</body>
</html>
```